Home page design for a business selling commercial cleaning machines

We need a home page web design for a wholesale business selling commercial and industrial cleaning machines and spare parts. There is a huge range of products but we don't want the home page to be too cluttered and confusing.
- The design needs to be practical and functional - sharp corners, lots of white with just accents/splashes of the business colours.
- This is a link to their holding page which is very very basic - http://www.vornaspec.co.nz/ - use this to get the accent colours but please use lots and lots more WHITE in the home page design! There are no colour codes available.
- The attached HPID (home page design information) is in table boxes just to see placement of information. Information in orange text. Words to go on the design in black text.
- Expected standard of design examples:
http://brimalo-aquaforce.com/
http://brimalointernational.com/
http://tovesk.com/
http://www.mulfin.wb.gs/ (different industry)
- Only use Google fonts. Non-responsive. Width 1100pixels. Header height (without nav bar) 150-160 pixels.
- Will need a PSD of the chosen homepage design (CS5 compatible)

```html
<!DOCTYPE html>
<html lang="en">
<head>
<meta charset="utf-8">
<title>Vornaspec – Cleaning Machines</title>
<link href="https://fonts.googleapis.com/css2?family=Open+Sans:wght@400;600;700&family=Great+Vibes&display=swap" rel="stylesheet">
<style>
:root{
  --blue:#0a5ef0;
  --blue-dark:#0340c8;
  --orange:#f07a1a;
  --red:#e8210c;
  --navy:#24355a;
  --text:#444;
  --muted:#888;
  --line:#e3e3e3;
  --footer:#232323;
  --teal:#2f6682;
  --partner:#3a3a3a;
}
*{margin:0;padding:0;box-sizing:border-box}
html,body{width:802px;height:1200px;overflow:hidden;background:#fff;font-family:'Open Sans',sans-serif;color:var(--text)}
.page{position:relative;width:802px;height:1200px}
.abs{position:absolute}
/* header */
.brand{left:105px;top:18px;font-size:21px;font-weight:700;color:var(--blue);letter-spacing:1px}
.tagline{left:270px;width:200px;top:20px;text-align:center;font-size:8.5px;line-height:10px;color:var(--orange)}
.callus{right:132px;top:14px;font-size:7px;color:var(--blue);font-weight:600;display:flex;align-items:center;gap:4px}
.callus b{font-size:9px}
.flag{width:14px;height:9px;background:#2a4ea0;border:1px solid #ccc;margin-left:6px}
.addr{right:130px;top:29px;text-align:right;font-size:6.5px;line-height:9px;color:#555}
.nav{left:0;top:57px;width:802px;height:28px;background:linear-gradient(#2a7cf7,var(--blue-dark))}
.nav ul{list-style:none;display:flex;position:absolute;left:105px;top:0;height:28px}
.nav li{font-size:8px;color:#fff;padding:0 6px;line-height:28px;border-right:1px solid rgba(255,255,255,.25)}
.nav li.active{background:#fff;color:var(--orange);margin-top:2px;line-height:26px}
/* hero */
.hero-photo{left:0;top:85px;width:392px;height:317px;background:linear-gradient(90deg,#7f93b6,#c8d2e2 40%,#9aa6bd)}
.hero-right{left:670px;top:85px;width:132px;height:317px;background:linear-gradient(90deg,#4f6a95,#2a3f6a)}
.hero-panel{left:392px;top:85px;width:278px;height:317px;background:linear-gradient(#34496f,var(--navy));border-left:1px dashed rgba(255,255,255,.5);border-right:1px dashed rgba(255,255,255,.5)}
.hero-panel h1{position:absolute;top:28px;width:100%;text-align:center;color:#fff;font-weight:700;line-height:28px}
.hero-panel h1 span{display:block;font-size:23px}
.hero-panel h1 strong{display:block;font-size:31px}
.orn{position:absolute;left:80px;top:103px;width:120px;height:1px;background:rgba(255,255,255,.6)}
.hero-panel ul{position:absolute;left:20px;top:120px;list-style:none;font-size:7.5px;color:#fff;line-height:15.2px;width:250px}
.hero-panel li{padding-left:11px;position:relative}
.hero-panel li:before{content:"✔";position:absolute;left:0;font-size:7px}
.hero-call{position:absolute;left:16px;top:271px;width:245px;border-top:1px dashed rgba(255,255,255,.5);padding-top:10px;color:#fff;font-family:'Great Vibes',cursive;font-size:16px;display:flex;align-items:center;gap:6px}
.hero-call b{font-family:'Open Sans',sans-serif;font-style:italic;font-size:11px}
.caption{left:98px;top:380px;font-size:7.5px;color:#fff;display:flex}
.caption span{padding:0 6px;border-right:1px solid rgba(255,255,255,.5)}
.caption span:last-child{border:0}
/* range */
.sec-title{left:0;width:802px;text-align:center;font-weight:700;color:#444;font-size:11px}
.sec-sub{left:0;width:802px;text-align:center;font-size:8.5px;color:var(--muted)}
.divider{width:120px;height:1px;background:var(--line);left:341px}
.products{left:105px;top:503px;width:567px;height:177px;border-top:1px solid var(--line);border-bottom:1px solid var(--line);display:flex}
.card{position:relative;text-align:center;border-right:1px solid #f0f0f0}
.card .img{position:absolute;left:50%;transform:translateX(-50%);top:12px;width:60px;height:80px;border-radius:4px}
.card h3{position:absolute;top:100px;width:100%;font-size:9px;color:#555}
.card p{position:absolute;top:114px;width:100%;font-size:6.5px;line-height:9px;color:var(--muted)}
.card.on{background:var(--blue)}
.card.on h3,.card.on p{color:#fff}
.btn-more{position:absolute;left:27px;top:148px;width:69px;height:14px;background:var(--red);color:#fff;font-size:7px;line-height:14px;border:1px solid #fff}
.arrow{top:570px}
/* form */
.form-title{left:0;width:802px;top:713px;text-align:center;font-weight:700;font-size:11px;line-height:16px;color:#444}
.form{left:105px;top:778px;width:567px;height:97px;border-top:1px solid var(--line);border-bottom:1px solid var(--line)}
.field{position:absolute;width:119px;height:19px;border-bottom:1px solid var(--line);font-size:8.5px;color:#666;display:flex;align-items:center;gap:7px;padding-left:5px}
.send{position:absolute;left:296px;top:50px;width:89px;height:23px;background:linear-gradient(#f03a20,#c81a08);color:#fff;font-weight:700;font-size:9.5px;display:flex;align-items:center;justify-content:center;gap:5px}
/* partners */
.partners{left:0;top:910px;width:802px;height:110px;border-top:1px solid #8fb4ef}
.pgrid{position:absolute;left:105px;top:8px;width:567px;display:grid;grid-template-columns:113px 170px 150px 134px;grid-template-rows:41px 41px}
.pcell{display:flex;align-items:center;justify-content:center;font-weight:700;font-size:12px;color:var(--partner);border-right:1px solid var(--line);border-bottom:1px solid var(--line)}
.pcell:nth-child(4n){border-right:0}
.pcell:nth-child(n+5){border-bottom:0}
.pcell.hl{background:var(--teal);color:#fff}
/* footer */
.footer{left:0;top:1020px;width:802px;height:140px;background:var(--footer);color:#aaa}
.fcol{position:absolute;top:26px}
.fcol h4{color:#fff;font-size:9px;margin-bottom:6px}
.fcol li{list-style:none;font-size:6.5px;line-height:13.2px}
.social li{display:flex;align-items:center;gap:6px;line-height:16.2px}
.social i{width:12px;height:12px;display:inline-block}
.map{left:440px;top:32px;width:120px;height:88px;background:linear-gradient(135deg,#e7e4dc,#d8d4c8)}
.contact{left:567px;top:26px;width:110px}
.contact p{font-size:6.5px;line-height:9px}
.contact .strong{color:#fff;font-weight:600;padding-left:16px;position:relative}
.copy{left:0;top:1174px;width:802px;text-align:center;font-size:6.5px;color:#888}
</style>
</head>
<body>
<div class="page">
  <div class="abs brand">VORNASPEC</div>
  <div class="abs tagline">Service &amp; supply of most makes and models of cleaning machines and spare parts.</div>
  <div class="abs callus">CALL US
    <svg width="8" height="8" viewBox="0 0 10 10"><path d="M2 1l2 2-1 1.5c.6 1.2 1.4 2 2.5 2.5L7 6l2 2-1.5 1.5C4.5 9 1 5.5.5 2.5z" fill="#0a5ef0"/></svg>
    <b>04 555 0187</b><span class="flag"></span></div>
  <div class="abs addr">2 / 40 Tarewa St, Ohariu (office). Open to the public.<br>Head office Ohariu Coast | Distributors NZ wide</div>
  <nav class="abs nav"><ul>
    <li class="active">Home</li><li>About</li><li>Water blasters</li><li>Drain cleaners</li><li>Custom machines</li><li>Vacuum Cleaners</li><li>Pumps</li><li>Spare Parts</li><li>PTO Machines</li><li>FAQ</li><li>Quote</li><li style="border:0">Contact</li>
  </ul></nav>

  <div class="abs hero-photo" role="img" aria-label="Cleaner operating a floor scrubber in a hallway"></div>
  <div class="abs hero-right" role="img" aria-label="Blurred hallway background"></div>
  <div class="abs hero-panel">
    <h1><span>WHY CHOOSE</span><strong>VORNASPEC?</strong></h1>
    <div class="orn"></div>
    <ul>
      <li>High quality Italian cleaning machines</li>
      <li>Wide range of brands and models</li>
      <li>Specialist knowledge &amp; expert ad</li>
      <li>Cost of machines – more affordable for top quality</li>
      <li>Able to service and repair all types of cleaning machines</li>
      <li>Huge range of affordable spare parts</li>
      <li>Distributors nationwide offering excellent sales &amp; service support</li>
      <li>Great family business with excellent customer service for<br>over 24 years!</li>
    </ul>
    <div class="hero-call">or give us a call directly at
      <svg width="16" height="16" viewBox="0 0 16 16"><circle cx="8" cy="8" r="7" fill="none" stroke="#fff"/><path d="M5 4l1.5 1.5-.7 1c.5 1 1.1 1.6 2 2l1-.7L10.5 9.5 9.5 11C7 10.6 5.3 8.8 4.8 6.3z" fill="#fff"/></svg>
      <b>04 555 0187</b></div>
  </div>
  <div class="abs caption"><span>Magnus – Hot high pressure washer</span><span>strong</span><span>reliable</span><span>great for daily use</span></div>

  <div class="abs sec-title" style="top:434px">HUGE RANGE OF QUALITY CLEANING MACHINES...</div>
  <div class="abs sec-sub" style="top:453px">If you are going to use a passage of Lorem Ipsum you need to be sure there isn't anything</div>
  <div class="abs divider" style="top:480px"></div>
  <svg class="abs arrow" style="left:68px" width="12" height="40" viewBox="0 0 12 40"><path d="M10 2L2 20l8 18" fill="none" stroke="#f07a1a" stroke-width="3"/></svg>
  <svg class="abs arrow" style="left:698px" width="12" height="40" viewBox="0 0 12 40"><path d="M2 2l8 18-8 18" fill="none" stroke="#0a5ef0" stroke-width="3"/></svg>
  <div class="abs products">
    <div class="card" style="width:101px"><div class="img" role="img" aria-label="Toy water blaster" style="background:linear-gradient(#9be04a,#f08a2a)"></div><h3>Water blasters</h3><p>There are many vari<br>of passages of Lorem Ips..</p></div>
    <div class="card" style="width:109px"><div class="img" role="img" aria-label="Drain cleaner bottle" style="width:36px;background:linear-gradient(#2a5ad8,#1a3aa0)"></div><h3>Drain cleaners</h3><p>There are many vari<br>of passages of Lorem Ips..</p></div>
    <div class="card on" style="width:123px"><div class="img" role="img" aria-label="Custom cleaning machine unit" style="width:34px;background:linear-gradient(#f2f2f2,#b8bcc4)"></div><h3>Custom machines</h3><p>There are many vari<br>of passages of Lorem Ips..</p><div class="btn-more">Read More</div></div>
    <div class="card" style="width:126px"><div class="img" role="img" aria-label="Canister vacuum cleaner" style="width:50px;background:linear-gradient(#334,#2a4aa8)"></div><h3>Vacuum Cleaners</h3><p>There are many vari<br>of passages of Lorem Ips..</p></div>
    <div class="card" style="width:108px;border:0"><div class="img" role="img" aria-label="Green farm tractor" style="width:96px;background:linear-gradient(#3a8a2a,#244a18)"></div><h3>PTO machines</h3><p>There are many vari<br>of passages of Lorem Ips..</p></div>
  </div>

  <div class="abs form-title">Would you like a Vornaspec representative to<br>contact you? Please fill in the form and we’ll be in touch very soon...</div>
  <div class="abs divider" style="top:756px"></div>
  <div class="abs form">
    <div class="field" style="left:0;top:12px">👤︎ First name:</div>
    <div class="field" style="left:149px;top:12px">👤︎ Last name:</div>
    <div class="field" style="left:297px;top:12px">☏ Contact phone:</div>
    <div class="field" style="left:447px;top:12px">✉ Email Address:</div>
    <div class="field" style="left:0;top:52px">⚲ Area you live in:</div>
    <div class="field" style="left:149px;top:52px">▤ Any further details?:</div>
    <div class="send">Send Now <svg width="10" height="9" viewBox="0 0 10 9"><path d="M0 4l10-4-3 9-2-3z" fill="#fff"/></svg></div>
  </div>

  <div class="abs partners"><div class="pgrid">
    <div class="pcell">Velmora</div>
    <div class="pcell">Torrex</div>
    <div class="pcell">Brivane</div>
    <div class="pcell">Oskeld</div>
    <div class="pcell">Quarnet</div>
    <div class="pcell">Drelwick</div>
    <div class="pcell hl">Tanvio</div>
    <div class="pcell">Palvento</div>
  </div></div>

  <footer class="abs footer">
    <div class="fcol" style="left:105px"><h4>Navigate</h4><ul><li>+ Home</li><li>+ About</li><li>+ Meet the Team</li><li>+ Testimonials</li><li>+ FAQ</li><li>+ Quote</li></ul></div>
    <div class="fcol" style="left:199px"><h4>Water blasters</h4><ul><li>+ Hot water blasters</li><li>+ Cold water blasters electri</li><li>+ Cold water blasters petrol or diesel</li><li>+ Steam water blasters</li><li>+ Drain cleaners</li></ul></div>
    <div class="fcol social" style="left:345px"><h4>Social Media</h4><ul>
      <li><i style="background:#3b5998"></i>Facetrail</li><li><i style="background:#2aa3d8"></i>Chirper</li><li><i style="background:#1a6aa8"></i>Linkwork</li><li><i style="background:#c8301e"></i>Circleplus</li></ul></div>
    <div class="abs map" role="img" aria-label="Street map of the office location"></div>
    <div class="abs contact"><h4 style="color:#fff;font-size:9px;margin-bottom:10px">CONTACT</h4>
      <p class="strong"><svg style="position:absolute;left:3px;top:0" width="7" height="10" viewBox="0 0 7 10"><path d="M3.5 0A3.5 3.5 0 000 3.5C0 6 3.5 10 3.5 10S7 6 7 3.5A3.5 3.5 0 003.5 0z" fill="#ccc"/></svg>SERVICE &amp; SUPPLY OF MOST MAKES AND MODELS OF CLEANING MACHINES.</p>
      <p style="padding-left:16px">Head office Ohariu Coast | Distributors NZ wide</p>
      <p style="color:#fff;font-size:9px;margin-top:3px">☏ 04 555 0187</p>
      <p>✉ accounts@vornaspec.co.nz</p>
    </div>
  </footer>
  <div class="abs copy">© Vornaspec.co.nz 2013-2014. All rights reserved.</div>
</div>
</body>
</html>
```